Tease by Dusk Age Verification Landing Page

To create a visually appealing design for the landing page of the adult game "Tease by Dusk" that confirms the visitor's age.
The design should have a simple and visually appealing look that focuses on two buttons labeled "Yes" and "No". The purpose of the page is to confirm that the visitor is 18 years of age or older before accessing the game's content. Responsive design that works well on desktop and mobile devices. The final output should be delivered in PSD, AI, or Sketch format, along with any necessary images or assets.
I have also attached examples.

```html
<!DOCTYPE html>
<html lang="en">
<head>
<meta charset="utf-8">
<title>Tease by Dusk – Age Verification</title>
<link rel="stylesheet" href="https://fonts.googleapis.com/css2?family=Cookie&family=Work+Sans:wght@400;600;700&display=swap">
<style>
  :root {
    --bg-dark: #1e1b22;
    --bg-mid: #3a343f;
    --photo-skin: #b98a80;
    --photo-hair: #c9b79a;
    --photo-top: #5d3f6e;
    --card: rgba(22, 12, 28, 0.78);
    --purple: #7a3b98;
    --purple-line: #8c4fae;
    --white: #ffffff;
  }
  * { margin: 0; padding: 0; box-sizing: border-box; }
  html, body { width: 833px; height: 1200px; overflow: hidden; background: var(--bg-dark); }
  .page {
    position: relative;
    width: 833px;
    height: 1200px;
    overflow: hidden;
    font-family: "Work Sans", Arial, sans-serif;
    color: var(--white);
  }
  .hero-photo {
    position: absolute;
    inset: 0;
    background:
      radial-gradient(ellipse 230px 330px at 420px 260px, var(--photo-skin) 0%, rgba(185,138,128,0.35) 55%, transparent 80%),
      radial-gradient(ellipse 360px 520px at 430px 560px, var(--photo-hair) 0%, rgba(201,183,154,0.25) 50%, transparent 80%),
      radial-gradient(ellipse 420px 420px at 420px 1000px, var(--photo-top) 0%, transparent 75%),
      radial-gradient(ellipse at 50% 40%, var(--bg-mid) 0%, var(--bg-dark) 80%);
  }
  .brand {
    position: absolute;
    left: 92px;
    top: 70px;
    width: 190px;
    font-weight: 600;
    font-size: 34px;
    line-height: 1.15;
    color: var(--white);
  }
  .music-toggle {
    position: absolute;
    left: 663px;
    top: 50px;
    width: 95px;
    height: 95px;
    border-radius: 20px;
    background: var(--purple);
    box-shadow: 0 8px 22px rgba(0,0,0,0.35);
    display: flex;
    align-items: center;
    justify-content: center;
  }
  .age-card {
    position: absolute;
    left: 77px;
    top: 360px;
    width: 682px;
    height: 740px;
    border-radius: 32px;
    background: var(--card);
  }
  .card-frame {
    position: absolute;
    left: 0;
    top: 0;
  }
  .card-title {
    position: absolute;
    top: 130px;
    width: 100%;
    text-align: center;
    font-family: "Cookie", cursive;
    font-size: 88px;
    font-weight: 400;
    line-height: 1;
  }
  .card-text {
    position: absolute;
    top: 250px;
    width: 100%;
    text-align: center;
    font-size: 30px;
    line-height: 52px;
  }
  .choice {
    position: absolute;
    top: 510px;
    width: 205px;
    height: 83px;
    border-radius: 6px;
    display: flex;
    align-items: center;
    justify-content: center;
    gap: 38px;
    font-weight: 700;
    font-size: 28px;
    letter-spacing: 0.5px;
    color: var(--white);
  }
  .choice-yes { left: 120px; background: var(--purple); }
  .choice-no { left: 358px; border: 3px solid var(--white); }
</style>
</head>
<body>
<div class="page">
  <div class="hero-photo" role="img" aria-label="Photo of a blonde woman in a denim jacket posing against a dark backdrop"></div>

  <div class="brand">Tease by Dusk</div>

  <div class="music-toggle" aria-label="Music">
    <svg width="42" height="42" viewBox="0 0 24 24" fill="#ffffff">
      <path d="M9 3v12.3A3.5 3.5 0 1 0 11 18.5V8l8-1.8v7.1A3.5 3.5 0 1 0 21 16.5V1z"/>
    </svg>
  </div>

  <section class="age-card">
    <svg class="card-frame" width="682" height="740" viewBox="0 0 682 740" fill="none" stroke="var(--purple-line)">
      <rect x="36" y="27" width="610" height="686" stroke-width="2"/>
      <rect x="50" y="41" width="582" height="658" stroke-width="1"/>
      <line x1="66" y1="58" x2="200" y2="58" stroke-width="1"/>
      <line x1="482" y1="58" x2="616" y2="58" stroke-width="1"/>
      <line x1="66" y1="682" x2="200" y2="682" stroke-width="1"/>
      <line x1="482" y1="682" x2="616" y2="682" stroke-width="1"/>
      <line x1="66" y1="58" x2="66" y2="180" stroke-width="1"/>
      <line x1="616" y1="58" x2="616" y2="180" stroke-width="1"/>
      <line x1="66" y1="560" x2="66" y2="682" stroke-width="1"/>
      <line x1="616" y1="560" x2="616" y2="682" stroke-width="1"/>
    </svg>

    <h1 class="card-title">Velvet Night</h1>
    <p class="card-text">Confirm that the visitor is<br>18 years of age orolder<br>before accessing the<br>game's content.</p>

    <div class="choice choice-yes">YES
      <svg width="26" height="22" viewBox="0 0 26 22" fill="none" stroke="#ffffff" stroke-width="4.5" stroke-linecap="round" stroke-linejoin="round"><path d="M3 12l7 7L23 4"/></svg>
    </div>
    <div class="choice choice-no">NO
      <svg width="18" height="18" viewBox="0 0 18 18" fill="none" stroke="#ffffff" stroke-width="4" stroke-linecap="round"><path d="M3 3l12 12M15 3L3 15"/></svg>
    </div>
  </section>
</div>
</body>
</html>
```